TEK Logistics - Banner 2.5' x 8' for 20+ locations

Need a banner designed that will pop. This banner will be displayed at over 20 of our transportation facilities. Goal is for the banner to grab the attention of employees, contractors and clients and help reinforce our mission and core values. Designed needs to include TEK Logo, our core values and mission statement. Red and Black are the main company colors and we need to stay within that theme and color pallet. Attached is a previous version that was too basic and boring. Willing to consider a design that excludes the mission statement.

Gathering more feedback

```html
<!DOCTYPE html>
<html lang="en">
<head>
<meta charset="utf-8">
<title>TEK Logistics – Core Values Banner</title>
<link rel="stylesheet" href="https://fonts.googleapis.com/css2?family=Barlow:wght@600;700&family=Barlow+Condensed:wght@700&family=Yellowtail&display=swap">
<style>
  :root {
    --stage: #808084;
    --paper: #ffffff;
    --panel: #e7e8ea;
    --red: #d42a2a;
    --ink: #2b2a28;
    --white: #ffffff;
  }
  * { box-sizing: border-box; margin: 0; padding: 0; }
  html, body { width: 1200px; height: 600px; overflow: hidden; background: var(--stage); }
  .canvas { position: relative; width: 1200px; height: 600px; }

  .banner {
    position: absolute; left: 150px; top: 160px;
    width: 900px; height: 281px; background: var(--paper);
  }
  .accent { position: absolute; }
  .accent--top { left: 470px; top: 0; }
  .accent--bottom { left: 208px; bottom: 0; }

  .brand-panel {
    position: absolute; left: 31px; top: 26px;
    width: 264px; height: 228px; background: var(--panel);
    display: flex; flex-direction: column; justify-content: center; align-items: center;
  }
  .brand-name {
    font-family: "Barlow", sans-serif; font-weight: 700;
    color: var(--red); text-align: center; line-height: 1;
  }
  .brand-name__main { display: block; font-size: 72px; letter-spacing: 2px; }
  .brand-name__sub { display: block; font-size: 25px; letter-spacing: 6px; margin-top: 4px; }

  .values {
    position: absolute; left: 299px; top: 26px;
    width: 571px; height: 228px;
    display: grid; grid-template-columns: repeat(3, 188px); grid-template-rows: repeat(2, 112px);
    column-gap: 3.5px; row-gap: 4px;
  }
  .value {
    display: flex; flex-direction: column; justify-content: center;
    color: var(--white); text-transform: uppercase; line-height: 0.92;
  }
  .value--red { background: var(--red); }
  .value--dark { background: var(--ink); }
  .value__small { font-family: "Barlow", sans-serif; font-weight: 600; font-size: 15.5px; }
  .value__big { font-family: "Barlow Condensed", sans-serif; font-weight: 700; font-size: 25px; }
  .value__and { font-family: "Barlow", sans-serif; font-weight: 600; font-size: 15.5px; }

  .value--right-things { padding-left: 21px; }
  .value--growth { padding-left: 25px; }
  .value--wow { padding-left: 30px; }
  .value--team { padding-left: 19px; }
  .value--safety { padding-left: 25px; }
  .value--fun { align-items: center; }
  .value__script {
    font-family: "Yellowtail", cursive; font-size: 38px; text-transform: none;
    line-height: 1; padding-left: 6px;
  }
</style>
</head>
<body>
<div class="canvas">
  <section class="banner">
    <svg class="accent accent--top" width="222" height="19" viewBox="0 0 222 19" aria-hidden="true">
      <polygon points="19,0 222,0 203,19 0,19" fill="var(--red)"/>
    </svg>
    <svg class="accent accent--bottom" width="222" height="19" viewBox="0 0 222 19" aria-hidden="true">
      <polygon points="19,0 222,0 203,19 0,19" fill="var(--ink)"/>
    </svg>

    <div class="brand-panel">
      <h1 class="brand-name">
        <span class="brand-name__main">TEK</span>
        <span class="brand-name__sub">LOGISTICS</span>
      </h1>
    </div>

    <div class="values">
      <div class="value value--dark value--right-things">
        <span class="value__small">Do the</span>
        <span class="value__big">Right Things</span>
        <span class="value__small">For the</span>
        <span class="value__big">Right Reasons</span>
      </div>
      <div class="value value--red value--growth">
        <span class="value__small">Pursue</span>
        <span class="value__big">Growth <span class="value__and">and</span></span>
        <span class="value__big">Development</span>
      </div>
      <div class="value value--dark value--wow">
        <span class="value__big">Deliver Wow</span>
        <span class="value__small">Through</span>
        <span class="value__big">Service</span>
      </div>
      <div class="value value--red value--team">
        <span class="value__small">Build a</span>
        <span class="value__big">Positive Team</span>
        <span class="value__small">Atmosphere</span>
      </div>
      <div class="value value--dark value--safety">
        <span class="value__big">Do Everything</span>
        <span class="value__big">Safely</span>
      </div>
      <div class="value value--red value--fun">
        <span class="value__script">Have Fun</span>
      </div>
    </div>
  </section>
</div>
</body>
</html>
```